FREE Network Assessment image for landing page

This graphic will be on a landing page and on the left will be Text and a download button that we change and control. The graphic for this project will be to the right.
I will add an example of the landing page area so that it makes more sense.

Please include the text from the sample - the font needs to be the same style as what we are using on the left side!

The graphic needs to be a .png file, roughly 713 x 527 white background. Use discretion on design layout.

Colors are black, Red = PMS 1795 and Gray = Cool Gray 10

Thanks,
Tom Farrow

Target Market(s)

small businesses

Industry/Entity Type

Information Technology

Font styles to use
Other font styles liked:
• See sample

Requirements
Must have
• see description
Nice to have
• Possibly small technology related image to help enhance the text but I don't want any image to compete with the text. Keep in mind the colors mentioned in the description - this is the web site colors.
Should not have
• Should not be hard to read

```html
<!DOCTYPE html>
<html lang="en">
<head>
<meta charset="utf-8">
<title>Free Network Health Assessment Tool</title>
<link rel="stylesheet" href="https://fonts.googleapis.com/css2?family=Oswald:wght@300;400;500;600&display=swap">
<style>
  :root {
    --red: #e8272c;
    --ink: #474a54;
    --ink-soft: #5a5d66;
    --panel: #f3f4f5;
    --page: #ffffff;
    --nav-top: #f1f1f2;
    --nav-bottom: #a9aaad;
    --dot: #c4c5c8;
    --network: #cfdcea;
  }
  * { box-sizing: border-box; margin: 0; padding: 0; }
  html, body {
    width: 1200px; height: 1000px; overflow: hidden;
    background: var(--page);
    font-family: "Oswald", sans-serif;
    color: var(--ink);
  }
  .frame {
    position: absolute; left: 179px; top: 186px;
    width: 844px; height: 630px;
    border: 12px solid var(--red);
    background: var(--panel);
    overflow: hidden;
  }
  .frame > * { position: absolute; }
  .search { left: 639px; top: 36px; display: flex; align-items: center; gap: 4px; }
  .search-field {
    width: 113px; height: 14px;
    border: 1px solid #9c9da0;
    background: linear-gradient(#d6d7d9, #eeeff0);
  }
  .search-label { font-size: 8px; font-weight: 500; color: #222; letter-spacing: .2px; }
  .main-nav {
    left: 18px; top: 61px; width: 786px; height: 36px;
    display: flex; gap: 2px; list-style: none;
  }
  .main-nav li {
    height: 100%; display: flex; align-items: center; justify-content: center;
    background: linear-gradient(var(--nav-top), var(--nav-bottom));
    font-size: 13.5px; color: var(--ink);
  }
  .hero-title {
    left: 46px; top: 140px;
    font-size: 47px; font-weight: 400; line-height: 47px;
    letter-spacing: -.3px;
  }
  .hero-title span { display: block; }
  .hero-lead {
    left: 46px; top: 265px; width: 450px;
    font-size: 18.5px; font-weight: 300; line-height: 22px;
    color: var(--ink-soft); letter-spacing: .2px;
  }
  .cta {
    left: 46px; top: 354px; width: 190px; height: 38px;
    border-radius: 19px; background: var(--red); color: #fff;
    display: flex; align-items: center; justify-content: center;
    font-size: 15px; font-weight: 400; text-decoration: none;
  }
  .slider-dots { left: 296px; top: 362px; display: flex; align-items: center; gap: 22px; }
  .slider-dots span { width: 10px; height: 10px; border-radius: 50%; background: var(--dot); }
  .slider-dots .active { width: 18px; height: 18px; background: var(--red); border: 4px solid var(--dot); }
  .checklist-block { left: 63px; top: 438px; width: 420px; }
  .checklist-title { font-size: 11px; font-weight: 400; margin-bottom: 10px; }
  .checklist { list-style: none; }
  .checklist li {
    display: flex; align-items: center; gap: 7px;
    font-size: 8.2px; font-weight: 400; line-height: 14.3px; color: #333;
  }
  .checklist svg { width: 10px; height: 9px; flex: none; }
  .book-link { display: block; margin-top: 9px; font-size: 10px; font-weight: 600; color: var(--red); text-decoration: none; }
  .network-art {
    left: 527px; top: 140px; width: 320px; height: 358px;
    background: radial-gradient(circle at 50% 50%, transparent 0 34%, var(--network) 38% 62%, transparent 66%);
    border-radius: 50%; opacity: .75;
  }
</style>
</head>
<body>
  <section class="frame">
    <form class="search">
      <div class="search-field"></div>
      <span class="search-label">SEARCH</span>
      <svg width="14" height="13" viewBox="0 0 14 13" aria-hidden="true">
        <circle cx="5" cy="5" r="3.6" fill="none" stroke="#222" stroke-width="1.6"/>
        <line x1="7.8" y1="7.6" x2="12.5" y2="11.8" stroke="#222" stroke-width="2.2" stroke-linecap="round"/>
      </svg>
    </form>

    <ul class="main-nav">
      <li style="width:86px">HOME</li>
      <li style="width:86px">ABOUT</li>
      <li style="width:86px">TEAM</li>
      <li style="width:172px">WHAT MAKES US DIFFERENT</li>
      <li style="width:86px">SERVICES</li>
      <li style="width:86px">DEPARTMENTS</li>
      <li style="width:86px">BLOG</li>
      <li style="width:86px">CONTACTS</li>
    </ul>

    <div class="network-art" role="img" aria-label="Light blue network of connected nodes forming a ring"></div>

    <h1 class="hero-title"><span>FREE NETWORK HEALTH</span><span>ASSESSMENT TOOL</span></h1>

    <p class="hero-lead">Let us show you to find and get rid of computer and network slowness, security, vulnerabilities and potential disaster.</p>

    <a class="cta" href="#">MAKE AN APPOINMENT</a>

    <div class="slider-dots"><span></span><span></span><span class="active"></span></div>

    <div class="checklist-block">
      <h2 class="checklist-title">FREE Network &amp; Computer health check service</h2>
      <ul class="checklist">
        <li><svg viewBox="0 0 10 9"><path d="M1 5 L4 8 L9 1" fill="none" stroke="var(--red)" stroke-width="1.6"/></svg>Check your network's security against hacker attacks, theft, ransomware, viruses, and more.</li>
        <li><svg viewBox="0 0 10 9"><path d="M1 5 L4 8 L9 1" fill="none" stroke="var(--red)" stroke-width="1.6"/></svg>See who and what has access to your network and data.</li>
        <li><svg viewBox="0 0 10 9"><path d="M1 5 L4 8 L9 1" fill="none" stroke="var(--red)" stroke-width="1.6"/></svg>Perform network and Internet speed test</li>
        <li><svg viewBox="0 0 10 9"><path d="M1 5 L4 8 L9 1" fill="none" stroke="var(--red)" stroke-width="1.6"/></svg>Resolve PC slowness issues, security vulnerablities and improper configurations</li>
        <li><svg viewBox="0 0 10 9"><path d="M1 5 L4 8 L9 1" fill="none" stroke="var(--red)" stroke-width="1.6"/></svg>Validate your backups are working and recoverable in a timely fashion.</li>
      </ul>
      <a class="book-link" href="#">Book an appointment now!</a>
    </div>
  </section>
</body>
</html>
```